Tourism Marketing needing sleek, clear design for business card & proposal documents.

***Company background***
"Quiet Harbour" is a company specializing in tourism marketing and project management. We do international wholesale, event management as well as ongoing representation of tourism and hospitality companies.

***Target market***
We cater to tourism companies and hotel professionals.

***Task***
We would like to get a single sided business card designed (but will still consider two sided, we are open to any ideas you may have). The layout for this card should be modern and elegant. Currently we do not have a logo, but we would like our business name in a really simple typography for the business card (similar to Moonrise Palace's logo - www.moonrisepalace-example.com.au).We are after a design that is clear, strong enough to be recognised as Quiet Harbour that does not require any fancy design. Another option is a simple play on QH (Quiet Harbour) or simply have Quiet Harbour featured elsewhere on card more as a brand/logo.

Feel free to submit different fonts if you feel you have any other fonts/designs that may be suitable for this card other than sans serifs. Should this project be successful, we will be considering several other projects for business proposal templates and eventually a website design.

The information that needs to go on the card are as follows:

Marta Holloway
Director
Quiet Harbour
Tourism Marketing & Representation
87 Wendover Parade
Prahran, Victoria, 3181 Australia
T +61 498203617 E marta@quietharbour-example.com.au

***Look and feel***
We'd like the business card design to express the following:
Modern, sleek, elegant, simple, discreet, quality, subtle, professional, creative, innovation

In terms of typography, we like something really simple and blocky (similar font to Moonrise Palace's logo - www.moonrisepalace-example.com.au)

***Colour scheme***
Shades of grey and dark teal

***Note***
Although our main target market are professionals, we would like the business card design to be versatile enough to be used outside of the tourism industry and need to appeal to different markets.

I do not have existing logo. Was hoping for a design that may be clear, strong enough not to require one. Other option is a simple play on QH (Quiet Harbour) or simply have Quiet Harbour featured elsewhere on card more as a brand/logo.

Marta Holloway
Director
Quiet Harbour Pty Ltd 
87 Wendover Parade
T +61 498203617  E  marta@quietharbour-example.com.au

Thank you for designs so far. Many have used a mauve colour which matches our company profile. This is not necessary, as that is just a draft and will be completely redesigned, so dont  feel you need to incorporate the mauve.

My colour preferences are for a white or grey background, and I like fonts in dark teals, grey or other sophisticated but modern colours. feel free to submit different fonts if you you have other fonts you thing would be suitable for this card, along with sans serifs. Should this project be successful, we will be considering several others for business proposal templates and eventually website. 

Target Market(s)

International Hospitality Senior Executives, Directors of International Tourism Companies, Directors of Tourism Bodies Internationally, local Tourism

Industry/Entity Type

Hospitality

Requirements
Should not have
• must not have bright garish colour, swirly patterns or anything that dates too much.

```html
<!DOCTYPE html>
<html lang="en">
<head>
<meta charset="utf-8">
<title>Quiet Harbour – Business Card</title>
<link rel="stylesheet" href="https://fonts.googleapis.com/css2?family=Arimo:ital,wght@1,700&family=Marcellus+SC&display=swap">
<style>
  :root {
    --teal-deep: #0f4468;
    --teal-text: #124d76;
    --contact-blue: #17517d;
    --panel-black: #000000;
    --white: #ffffff;
    --mark-fill: #0e4468;
  }
  html, body {
    margin: 0;
    padding: 0;
    width: 1200px;
    height: 635px;
    overflow: hidden;
    background: var(--panel-black);
  }
  .card {
    position: relative;
    width: 1200px;
    height: 635px;
    overflow: hidden;
    background: var(--panel-black);
    font-family: "Arimo", Arial, sans-serif;
  }
  .card__upper {
    position: absolute;
    left: 0; top: 0;
    width: 1200px;
    height: 450px;
    background:
      linear-gradient(118deg, #f6f6f6 0%, #e2e3e4 22%, #b9bcbf 45%, #8a8f95 65%, #4b5259 84%, #1b2128 100%);
  }
  .card__divider {
    position: absolute;
    left: 0; top: 448px;
    width: 1200px;
    height: 6px;
    background: linear-gradient(180deg, #d8d8d8 0%, #9a9a9a 45%, #3a3a3a 100%);
  }
  .brand-dot {
    position: absolute;
    left: 90px; top: 102px;
    width: 160px; height: 160px;
  }
  .person {
    position: absolute;
    right: 80px;
    top: 48px;
    text-align: right;
    font-family: "Marcellus SC", "Copperplate", serif;
    color: var(--teal-deep);
    letter-spacing: 2px;
  }
  .person__name {
    margin: 0;
    font-size: 40px;
    font-weight: 400;
    line-height: 1;
  }
  .person__role {
    margin: 10px 8px 0 0;
    font-size: 32px;
    line-height: 1;
  }
  .brand {
    position: absolute;
    left: 0;
    top: 242px;
    width: 1146px;
    text-align: center;
  }
  .brand__name {
    margin: 0;
    font-size: 48px;
    font-weight: 700;
    font-style: italic;
    color: var(--teal-text);
    line-height: 1;
  }
  .brand__tagline {
    margin: 24px 0 0 34px;
    font-size: 25px;
    font-weight: 700;
    font-style: italic;
    color: var(--white);
    line-height: 1;
  }
  .contact {
    position: absolute;
    left: 39px;
    top: 490px;
    margin: 0;
    font-family: Arial, "Helvetica Neue", sans-serif;
    font-style: normal;
    font-size: 24px;
    line-height: 37px;
    color: var(--contact-blue);
    word-spacing: 8px;
  }
  .contact__line { display: block; }
  .contact__chip {
    display: inline-block;
    width: 24px; height: 24px;
    border-radius: 6px;
    background: #1f8fd6;
    vertical-align: -4px;
    margin: 0 2px 0 2px;
  }
</style>
</head>
<body>
  <main class="card">
    <div class="card__upper"></div>
    <div class="card__divider"></div>

    <svg class="brand-dot" viewBox="0 0 160 160" aria-hidden="true">
      <circle cx="80" cy="80" r="80" fill="var(--mark-fill)"/>
    </svg>

    <header class="person">
      <h1 class="person__name">Marta Holloway</h1>
      <p class="person__role">Director</p>
    </header>

    <section class="brand">
      <h2 class="brand__name">Quiet Harbour</h2>
      <p class="brand__tagline">Tourism Marketing &amp; Representation</p>
    </section>

    <address class="contact">
      <span class="contact__line">87 Wendover Parade</span>
      <span class="contact__line">Prahran, Victoria, 3181 Australia</span>
      <span class="contact__line">T<span class="contact__chip" aria-hidden="true"></span>+61 498203617 E marta@quietharbour-example.com.au</span>
    </address>
  </main>
</body>
</html>
```